business card logos

We have two companies
1) Velvet Route limos and our punch line is " Don't Just Hail it. Velvet Route it.

2) Copperleaf Chauffeur Cars and the punch line is " Yes, your travel is our business!"
We provide chauffeured cars in Sydney for corporate travel in the city's metropolitan areas. These are very comfortable and affordable corporate cars for our most valuable clients.

Need a logo design for business cards for both which will be unique, reflects the services we offer, has to look professional.

```html
<!DOCTYPE html>
<html lang="en">
<head>
<meta charset="utf-8">
<title>Velvet Route &amp; Copperleaf business cards</title>
<link rel="stylesheet" href="https://fonts.googleapis.com/css2?family=Gafata&family=Marcellus&family=Mr+Dafoe&display=swap">
<style>
  :root {
    --page: #ffffff;
    --velvet-band: #2d2a70;
    --velvet-glow: #4b4393;
    --velvet-badge: #2c3a98;
    --copper-band: #1e80c4;
    --copper-badge: #52a9e0;
    --copper-base: #29296a;
    --copper-glow: #1f5fb8;
    --ink-light: #ffffff;
    --ink-dark: #111111;
    --card-white: #ffffff;
    --car-dark: #1a1a1f;
    --car-mid: #4a4d57;
  }
  * { box-sizing: border-box; margin: 0; padding: 0; }
  html, body {
    width: 849px; height: 1200px; overflow: hidden;
    background: var(--page);
  }
  .sheet { position: relative; width: 849px; height: 1200px; }

  .card {
    position: absolute; left: 36px; width: 777px; height: 427px;
    overflow: hidden;
    box-shadow: 5px 5px 5px rgba(0, 0, 0, 0.45);
    font-family: "Gafata", sans-serif;
    color: var(--ink-light);
  }
  .card--velvet { top: 61px; background: var(--card-white); }
  .card--copper { top: 567px; background: var(--copper-base); }

  .card__band { position: absolute; left: 0; top: 0; width: 100%; height: 276px; }
  .card--velvet .card__band {
    background: radial-gradient(circle at 300px 190px, var(--velvet-glow) 0%, var(--velvet-band) 45%, var(--velvet-band) 100%);
  }
  .card--copper .card__band { background: var(--copper-band); }

  .card__glow {
    position: absolute; left: 314px; top: 74px; width: 160px; height: 120px;
    background: radial-gradient(ellipse at center, rgba(255,255,255,0.9) 0%, rgba(255,255,255,0.25) 25%, rgba(255,255,255,0) 65%);
  }

  .brand {
    position: absolute; width: 158px; height: 158px; border-radius: 50%;
    display: flex; align-items: center; justify-content: center;
    text-align: center; padding: 0 18px;
    box-shadow: 3px 4px 8px rgba(0, 0, 0, 0.35);
    font-size: 19px; line-height: 1.2; letter-spacing: 0.5px;
    text-transform: uppercase; color: var(--ink-light);
  }
  .card--velvet .brand { left: 9px; top: 5px; background: var(--velvet-badge); }
  .card--copper .brand { left: 9px; top: 9px; background: var(--copper-badge); }

  .contact {
    position: absolute; left: 230px; top: 38px; list-style: none;
  }
  .contact__item {
    display: flex; align-items: center; height: 28px; margin-bottom: 24px;
    font-size: 23px;
  }
  .contact__item svg { width: 16px; height: 16px; margin-right: 10px; flex: none; }

  .divider {
    position: absolute; left: 499px; top: 49px; width: 2px; height: 114px;
    background: var(--ink-light);
  }

  .person { position: absolute; left: 552px; top: 48px; width: 180px; text-align: center; }
  .person__name { font-size: 33px; line-height: 1.2; font-weight: 400; }
  .person__role { font-size: 20px; margin-top: 12px; }
  .card--velvet .person__name,
  .card--velvet .person__role { font-family: "Marcellus", serif; }

  .vehicle { position: absolute; }
  .card--velvet .vehicle {
    left: 29px; top: 322px; width: 410px; height: 76px;
    background: linear-gradient(180deg, var(--car-mid) 0%, var(--car-dark) 60%, var(--car-mid) 100%);
    border-radius: 14px 30px 10px 10px;
  }
  .card--copper .vehicle {
    left: 74px; top: 285px; width: 278px; height: 89px;
    background: radial-gradient(ellipse at center, var(--copper-glow) 0%, rgba(31,95,184,0) 70%);
  }
  .card--copper .card__base-glow {
    position: absolute; left: 0; top: 276px; width: 420px; height: 151px;
    background: radial-gradient(ellipse at 200px 70px, rgba(31,95,184,0.7) 0%, rgba(41,41,106,0) 70%);
  }

  .tagline { position: absolute; }
  .card--velvet .tagline {
    left: 492px; top: 310px; color: var(--ink-dark);
    font-family: "Mr Dafoe", cursive; font-size: 31px; line-height: 42px;
  }
  .card--velvet .tagline__second { padding-left: 16px; display: block; }
  .card--copper .tagline {
    left: 402px; top: 290px; font-size: 30px; line-height: 46px;
  }
</style>
</head>
<body>
<main class="sheet">

  <section class="card card--velvet" aria-label="Velvet Route limos business card">
    <div class="card__band"></div>
    <div class="brand">Velvet Route limos</div>

    <ul class="contact">
      <li class="contact__item">
        <svg viewBox="0 0 16 16" aria-hidden="true"><path d="M8 1a5 5 0 0 0-5 5c0 4 5 9 5 9s5-5 5-9a5 5 0 0 0-5-5zm0 7a2 2 0 1 1 0-4 2 2 0 0 1 0 4z" fill="#fff"/></svg>
        Adress goes here.
      </li>
      <li class="contact__item">
        <svg viewBox="0 0 16 16" aria-hidden="true"><path d="M4 2l2.5 2.5-1.3 1.8c.8 1.8 2.2 3.2 4 4l1.8-1.3L13.5 11.5 12 14C7 13.5 2.5 9 2 4z" fill="#fff"/></svg>
        + 000 000
      </li>
      <li class="contact__item">
        <svg viewBox="0 0 16 16" aria-hidden="true"><circle cx="8" cy="8" r="6.5" fill="none" stroke="#fff" stroke-width="1.5"/><path d="M1.5 8h13M8 1.5c-3 3.5-3 9.5 0 13M8 1.5c3 3.5 3 9.5 0 13" fill="none" stroke="#fff" stroke-width="1.2"/></svg>
        www.example.com
      </li>
      <li class="contact__item">
        <svg viewBox="0 0 16 16" aria-hidden="true"><rect x="1.5" y="3.5" width="13" height="9" fill="none" stroke="#fff" stroke-width="1.4"/><path d="M1.5 3.5L8 9l6.5-5.5" fill="none" stroke="#fff" stroke-width="1.4"/></svg>
        hello@example.com
      </li>
    </ul>

    <div class="divider"></div>
    <div class="person">
      <p class="person__name">John Doe</p>
      <p class="person__role">Chauffeur</p>
    </div>

    <div class="vehicle" role="img" aria-label="Side view illustration of a black stretch limousine"></div>
    <p class="tagline">Don't Just Hail it.<span class="tagline__second">Velvet Route it.</span></p>
  </section>

  <section class="card card--copper" aria-label="Copperleaf Chauffeur Cars business card">
    <div class="card__band"></div>
    <div class="card__glow"></div>
    <div class="brand">Copperleaf Chauffeur Cars</div>

    <ul class="contact">
      <li class="contact__item">
        <svg viewBox="0 0 16 16" aria-hidden="true"><path d="M8 1a5 5 0 0 0-5 5c0 4 5 9 5 9s5-5 5-9a5 5 0 0 0-5-5zm0 7a2 2 0 1 1 0-4 2 2 0 0 1 0 4z" fill="#fff"/></svg>
        Adress goes here.
      </li>
      <li class="contact__item">
        <svg viewBox="0 0 16 16" aria-hidden="true"><path d="M4 2l2.5 2.5-1.3 1.8c.8 1.8 2.2 3.2 4 4l1.8-1.3L13.5 11.5 12 14C7 13.5 2.5 9 2 4z" fill="#fff"/></svg>
        + 000 000
      </li>
      <li class="contact__item">
        <svg viewBox="0 0 16 16" aria-hidden="true"><circle cx="8" cy="8" r="6.5" fill="none" stroke="#fff" stroke-width="1.5"/><path d="M1.5 8h13M8 1.5c-3 3.5-3 9.5 0 13M8 1.5c3 3.5 3 9.5 0 13" fill="none" stroke="#fff" stroke-width="1.2"/></svg>
        www.example.com
      </li>
      <li class="contact__item">
        <svg viewBox="0 0 16 16" aria-hidden="true"><rect x="1.5" y="3.5" width="13" height="9" fill="none" stroke="#fff" stroke-width="1.4"/><path d="M1.5 3.5L8 9l6.5-5.5" fill="none" stroke="#fff" stroke-width="1.4"/></svg>
        hello@example.com
      </li>
    </ul>

    <div class="divider"></div>
    <div class="person">
      <p class="person__name">John Doe</p>
      <p class="person__role">Chauffeur</p>
    </div>

    <div class="card__base-glow"></div>
    <div class="vehicle" role="img" aria-label="White line drawing of a sedan car outline"></div>
    <p class="tagline">Yes,<br>your travel is our business!</p>
  </section>

</main>
</body>
</html>
```